One-Page Promo flyer for Keynote Speaker Profile

Our CEO speaks at professional conferences and business events. We need to create a one-pager to promote his profile to events companies so they may select him to speak at their professional and industry events. He is a paid speaker so this flyer will be used as a selling tool. Please see the brief document for more details. Key aspects that need to be highlighted: company name, left panel as per the brief document.
Target Market(s)
corporate, business, professionals
Industry/Entity Type
Events

```html
<!DOCTYPE html>
<html lang="en">
<head>
<meta charset="utf-8">
<title>Speaker Profile – Daniel Mercer Stone</title>
<link rel="stylesheet" href="https://fonts.googleapis.com/css2?family=PT+Sans:wght@400;700&family=Tinos&display=swap">
<style>
  :root {
    --brand-blue: #0b4f9c;
    --deep-blue: #0a3f86;
    --charcoal: #555759;
    --ink: #222426;
    --paper: #f3f3f3;
    --backdrop: #dfe4e5;
  }
  html, body {
    margin: 0;
    width: 1200px;
    height: 958px;
    overflow: hidden;
    background: var(--backdrop);
  }
  .flyer {
    position: absolute;
    left: 275px;
    top: 20px;
    width: 649px;
    height: 918px;
    background: var(--paper);
    overflow: hidden;
    font-family: "PT Sans", sans-serif;
    color: var(--ink);
  }
  .top-band { position: absolute; left: 0; top: 0; width: 100%; height: 23px; background: var(--charcoal); }
  .speaker-name {
    position: absolute; left: 35px; top: 40px; margin: 0;
    font-family: "Tinos", serif; font-weight: 400; font-size: 35px;
    color: var(--brand-blue); line-height: 1;
  }
  .speaker-role {
    position: absolute; left: 36px; top: 83px; margin: 0;
    font-size: 14px; letter-spacing: 2.4px; color: var(--ink); font-weight: 400;
  }
  .side-bar { position: absolute; left: 0; width: 66px; }
  .side-bar--about { top: 119px; height: 292px; background: var(--brand-blue); }
  .side-bar--topics { top: 432px; height: 154px; background: var(--brand-blue); }
  .side-bar--testimonials { top: 598px; height: 245px; background: var(--charcoal); }

  .about-title {
    position: absolute; left: 85px; top: 132px; margin: 0;
    font-family: "Tinos", serif; font-weight: 400; font-size: 32px;
    color: var(--brand-blue); line-height: 1;
  }
  .about-text {
    position: absolute; left: 85px; top: 178px; width: 330px; margin: 0;
    font-size: 12.4px; line-height: 15.6px; letter-spacing: -0.2px;
  }
  .line { display: block; white-space: nowrap; }

  .photo-frame {
    position: absolute; left: 441px; top: 113px; width: 208px; height: 306px;
    background: var(--charcoal);
  }
  .photo {
    position: absolute; left: 8px; top: 8px; right: 8px; bottom: 3px;
    background: linear-gradient(135deg, #1b1f6e 0%, #3a2aa8 45%, #7b3fd4 80%, #b86be8 100%);
  }
  .divider-line {
    position: absolute; left: 66px; top: 417px; width: 583px; height: 5px;
    background: var(--brand-blue);
  }
  .divider-glow {
    position: absolute; left: 0; top: 422px; width: 649px; height: 14px;
    background: linear-gradient(180deg, #9fb3c9 0%, #dfe6ee 60%, rgba(243,243,243,0) 100%);
  }

  .section-title {
    position: absolute; left: 85px; margin: 0;
    font-size: 16px; font-weight: 700; color: var(--deep-blue); line-height: 1;
  }
  .section-title--topics { top: 452px; text-transform: uppercase; }
  .section-title--testimonials { top: 613px; }

  .topic-list {
    position: absolute; left: 85px; top: 480px; right: 0; margin: 0;
    font-size: 12.4px; line-height: 15.6px; letter-spacing: -0.2px; overflow: hidden;
  }
  .testimonial-list {
    position: absolute; left: 86px; top: 639px; width: 540px; margin: 0;
    font-size: 12.4px; line-height: 15.6px; letter-spacing: -0.2px;
  }
  .quote-lead, .quote-source--blue { color: var(--deep-blue); }

  .bottom-waves { position: absolute; left: 0; bottom: 0; width: 649px; height: 95px; }
</style>
</head>
<body>
  <article class="flyer">
    <div class="top-band"></div>

    <h1 class="speaker-name">Daniel Mercer Stone</h1>
    <p class="speaker-role">MARKETING AND SALES STRATEGIT</p>

    <div class="side-bar side-bar--about"></div>
    <div class="side-bar side-bar--topics"></div>
    <div class="side-bar side-bar--testimonials"></div>

    <h2 class="about-title">About Daniel Mercer</h2>
    <p class="about-text">
      <span class="line">Daniel Mercer Stone is an internationally acclaimed</span>
      <span class="line">marketing and</span>
      <span class="line">sales strategist, author of eight books (including three</span>
      <span class="line">international bestsellers),</span>
      <span class="line">advisor to emerging companies, and professional speaker</span>
      <span class="line">on topics</span>
      <span class="line">including marketing, sales, and social media.</span>
      <span class="line">He is the #1 international bestselling author of The Open</span>
      <span class="line">Rules of</span>
      <span class="line">Marketing and PR, now in its fourth edition with more</span>
      <span class="line">than 300,000</span>
      <span class="line">copies sold in more than 25 languages from Bulgarian to</span>
      <span class="line">Vietnamese</span>
    </p>

    <div class="photo-frame">
      <div class="photo" role="img" aria-label="Photo of the speaker presenting on a conference stage under purple lighting"></div>
    </div>

    <div class="divider-line"></div>
    <div class="divider-glow"></div>

    <h3 class="section-title section-title--topics">Speaking Topics</h3>
    <p class="topic-list">
      <span class="line">OPEN RULES OF MARKETING &amp; PR:</span>
      <span class="line">How to use social media, blogs, news releases, online video, and viral marketing to reach buyers directly</span>
      <span class="line">GROW YOUR BUSINESS NOW:</span>
      <span class="line">How to instantly engage your market and connect with customers in real time</span>
      <span class="line">AGILE SELLING IN A REAL-TIME WORLD:</span>
      <span class="line">How to succeed in a world where buyers are now in charge</span>
    </p>

    <h3 class="section-title section-title--testimonials">Client Testimonals :-</h3>
    <p class="testimonial-list">
      <span class="line quote-lead">“Ranked number 3 in overall satisfaction among 224 presenters at the Northwind Systems Worldwide</span>
      <span class="line quote-lead">Partner Conference. Very impressive.</span>
      <span class="line">Thank you for delivering a session that our partners felt was very valuable. I look forward to</span>
      <span class="line">working with you next year.”</span>
      <span class="line quote-source--blue">–Laura Benton, Senior Partner Skills Development Manager, Northwind Systems</span>
      <span class="line">“The highest rated presenter at our Summit Business magazine ‘Sales and Marketing</span>
      <span class="line">Summit’ – in front of hundreds of our nation’s</span>
      <span class="line">top mid-market CEOs and executives—Daniel cut through the jargon and provided a practical</span>
      <span class="line">and example-filled presentation on how executives can actually utilize</span>
      <span class="line">the Web 2.0 revolution to drive business to their companies.”</span>
      <span class="line">–Victor Hale, CEO, Meridian Growth Inc., Summit Conference Group</span>
    </p>

    <svg class="bottom-waves" viewBox="0 0 649 95" preserveAspectRatio="none" aria-hidden="true">
      <path d="M0,0 C70,30 180,70 330,72 C460,74 560,55 649,50 L649,95 L0,95 Z" fill="var(--brand-blue)"/>
      <path d="M90,48 C230,20 400,10 560,22 C600,25 630,30 649,36" fill="none" stroke="var(--paper)" stroke-width="9"/>
      <path d="M150,58 C300,30 440,22 560,28 C600,30 630,34 649,40" fill="none" stroke="var(--paper)" stroke-width="4"/>
      <path d="M300,52 C420,26 540,16 649,30 L649,38 C540,26 420,34 300,52 Z" fill="var(--charcoal)"/>
      <path d="M100,50 C240,26 400,18 540,24" fill="none" stroke="var(--brand-blue)" stroke-width="6"/>
    </svg>
  </article>
</body>
</html>
```